Business Card Design

we are a small based family business that specialise in 12v led lights for kelvo caravans.
we also sell 12v switches, wire, circuit breakers, dimmers etc but our main line is LEDs.
We would like something that reflects the LED lighting on our cards.
www.willowtreeleds.com.au is where you can have a look at to get ideas, of our product.
I have attached the logo we generally use on all our tradio listings and is the main header on our website.

Look forward to seeing what your team comes up with.

Industry/Entity Type

Business

Contact Information for Business Card

Tam 0491 738 205
Cedarwood Vale QLD 4312

www.willowtreeleds.com

```html
<!DOCTYPE html>
<html lang="en">
<head>
<meta charset="utf-8">
<title>Willow Tree LEDs – Business Card</title>
<link rel="stylesheet" href="https://fonts.googleapis.com/css2?family=Open+Sans:wght@400;700&display=swap">
<style>
  :root {
    --page-bg: #e9e6e2;
    --card-white: #f7f7f7;
    --brand-red: #a52d16;
    --band-black: #111111;
    --ink: #141414;
    --text-light: #ffffff;
  }
  * { box-sizing: border-box; margin: 0; padding: 0; }
  html, body {
    width: 1200px; height: 900px; overflow: hidden;
    background: var(--page-bg);
    font-family: "Open Sans", Arial, sans-serif;
  }
  .canvas {
    width: 1200px; height: 900px;
    display: flex; align-items: center; justify-content: center;
  }
  .business-card {
    position: relative;
    width: 1000px; height: 572px;
    background: var(--card-white);
    overflow: hidden;
    box-shadow: 0 10px 30px rgba(0,0,0,0.18);
  }
  .card-shapes { position: absolute; inset: 0; }
  .holder {
    position: absolute; left: 70px; top: 90px;
    color: var(--text-light);
  }
  .holder-name { font-size: 34px; font-weight: 700; line-height: 1.15; }
  .holder-role { font-size: 27px; font-weight: 400; }
  .contact-list {
    position: absolute; left: 70px; bottom: 52px;
    list-style: none; color: var(--text-light);
    font-size: 21px; line-height: 1.32;
  }
  .contact-item { display: flex; align-items: flex-start; gap: 12px; }
  .contact-icon { flex: 0 0 22px; width: 22px; height: 22px; margin-top: 4px; }
  .brand {
    position: absolute; left: 640px; top: 190px;
    display: flex; align-items: center; gap: 16px;
  }
  .brand-mark {
    flex: 0 0 30px; width: 30px; height: 30px;
    background: var(--brand-red);
  }
  .brand-name {
    font-weight: 700; color: var(--ink);
    font-size: 48px; line-height: 1.1;
  }
</style>
</head>
<body>
<main class="canvas">
  <section class="business-card">
    <svg class="card-shapes" viewBox="0 0 1000 572" preserveAspectRatio="none" aria-hidden="true">
      <path fill="var(--band-black)" d="M0,0 H482 Q600,230 676,572 H0 Z"/>
      <path fill="var(--brand-red)" d="M0,0 H466 Q572,230 640,572 H0 Z"/>
    </svg>

    <div class="holder">
      <p class="holder-name">Reed Palmer</p>
      <p class="holder-role">Owner / C.E.O</p>
    </div>

    <ul class="contact-list">
      <li class="contact-item">
        <svg class="contact-icon" viewBox="0 0 22 22"><circle cx="11" cy="11" r="11" fill="#fff"/><path d="M11 4.5a4.5 4.5 0 0 0-4.5 4.5c0 3.4 4.5 8.5 4.5 8.5s4.5-5.1 4.5-8.5A4.5 4.5 0 0 0 11 4.5z" fill="var(--brand-red)"/><circle cx="11" cy="9" r="1.6" fill="#fff"/></svg>
        <span>Suite # 14, Harbour Bldg,<br>QLD 4312</span>
      </li>
      <li class="contact-item">
        <svg class="contact-icon" viewBox="0 0 22 22"><circle cx="11" cy="11" r="11" fill="#fff"/><path d="M7 5.5l2.2 0 1 3-1.4 1.1a7 7 0 0 0 3.6 3.6l1.1-1.4 3 1v2.2c0 .6-.5 1-1 1A10 10 0 0 1 6 6.5c0-.5.4-1 1-1z" fill="var(--brand-red)"/></svg>
        <span>0491 738 205</span>
      </li>
      <li class="contact-item">
        <svg class="contact-icon" viewBox="0 0 22 22"><circle cx="11" cy="11" r="11" fill="#fff"/><rect x="7.5" y="4.5" width="7" height="13" rx="1.5" fill="var(--brand-red)"/></svg>
        <span>0491 738 206</span>
      </li>
      <li class="contact-item">
        <svg class="contact-icon" viewBox="0 0 22 22"><circle cx="11" cy="11" r="11" fill="#fff"/><rect x="5.5" y="8" width="11" height="8" rx="1" fill="var(--brand-red)"/><rect x="7.5" y="5" width="7" height="3" fill="var(--brand-red)"/></svg>
        <span>0491 738 207</span>
      </li>
      <li class="contact-item">
        <svg class="contact-icon" viewBox="0 0 22 22"><circle cx="11" cy="11" r="11" fill="#fff"/><rect x="5" y="7" width="12" height="8.5" rx="1" fill="var(--brand-red)"/><path d="M5.5 7.5l5.5 4.5 5.5-4.5" fill="none" stroke="#fff" stroke-width="1.2"/></svg>
        <span>hello@willowtreeleds.com</span>
      </li>
      <li class="contact-item">
        <svg class="contact-icon" viewBox="0 0 22 22"><circle cx="11" cy="11" r="11" fill="#fff"/><g fill="none" stroke="var(--brand-red)" stroke-width="1.4"><circle cx="11" cy="11" r="6"/><ellipse cx="11" cy="11" rx="2.6" ry="6"/><path d="M5 11h12"/></g></svg>
        <span>www.willowtreeleds.com</span>
      </li>
    </ul>

    <div class="brand">
      <span class="brand-mark" aria-hidden="true"></span>
      <p class="brand-name">Willow Tree<br>LEDs</p>
    </div>
  </section>
</main>
</body>
</html>
```